Harbourlight ceramics Ltd
Stone and tile specialists
Simple
Colin Ashby-Rhodes
Director
Address not needed on the business card
colin@harbourlightceramics.example
www.harbourlightceramics.example
We also require an A4 folder promotional sheet, a letter head, complimentry slip and a van design.
Logo and the web address. All other info on the other side. In UK we say mob: instead of cell.

```html
<!DOCTYPE html>
<html lang="en">
<head>
<meta charset="utf-8">
<title>Harbourlight ceramics Ltd – Business Card</title>
<link rel="stylesheet" href="https://fonts.googleapis.com/css2?family=Open+Sans:wght@400;700&family=Tinos&display=swap">
<style>
  :root {
    --backdrop: #e9e9e9;
    --card: #ffffff;
    --panel-grey: #c4c4c4;
    --accent: #f26f16;
    --ink: #1d1d1d;
    --muted: #555555;
  }
  * { margin: 0; padding: 0; box-sizing: border-box; }
  html, body { width: 1200px; height: 852px; overflow: hidden; }
  body {
    background: var(--backdrop);
    position: relative;
    font-family: "Open Sans", Arial, sans-serif;
  }
  .card {
    position: absolute;
    top: 265px;
    width: 500px;
    height: 322px;
    background: var(--card);
    border-radius: 22px;
    overflow: hidden;
    box-shadow: 0 6px 18px rgba(0,0,0,0.15);
  }
  .card--front { left: 70px; }
  .card--back { left: 630px; }

  .card__panel { position: absolute; inset: 0; width: 100%; height: 100%; }

  .company-name {
    position: absolute;
    color: var(--ink);
    font-weight: 700;
    line-height: 1.2;
  }
  .card--front .company-name {
    left: 34px;
    top: 62px;
    font-size: 24px;
  }

  .back-identity {
    position: absolute;
    left: 0;
    right: 0;
    top: 50%;
    transform: translateY(-50%);
    text-align: center;
  }
  .back-identity .company-name {
    position: static;
    font-size: 30px;
  }
  .back-identity__web {
    margin-top: 14px;
    font-family: "Tinos", "Times New Roman", serif;
    font-size: 14px;
    color: var(--muted);
  }

  .person {
    position: absolute;
    left: 310px;
    top: 100px;
    text-align: center;
  }
  .person__name { font-size: 17px; font-weight: 700; color: var(--ink); white-space: nowrap; }
  .person__role { font-size: 11px; color: #ffffff; margin-top: 4px; }

  .contacts {
    position: absolute;
    left: 30px;
    bottom: 42px;
    list-style: none;
    font-family: "Tinos", "Times New Roman", serif;
    font-size: 12px;
    color: var(--muted);
  }
  .contacts li { display: flex; align-items: center; gap: 8px; margin-top: 5px; }
  .contacts svg { width: 11px; height: 11px; flex: none; }
</style>
</head>
<body>

<section class="card card--front" aria-label="Business card front">
  <svg class="card__panel" viewBox="0 0 500 322" preserveAspectRatio="none" aria-hidden="true">
    <polygon points="250,0 500,0 500,200 318,200" fill="var(--panel-grey)"/>
    <polyline points="240,0 306,208 500,208" fill="none" stroke="var(--accent)" stroke-width="9"/>
  </svg>

  <p class="company-name">Harbourlight<br>ceramics Ltd</p>

  <div class="person">
    <p class="person__name">Colin Ashby-Rhodes</p>
    <p class="person__role">Director</p>
  </div>

  <ul class="contacts">
    <li>
      <svg viewBox="0 0 12 12" aria-hidden="true"><rect x="3" y="0.5" width="6" height="11" rx="1.2" fill="var(--accent)"/><rect x="4.2" y="2" width="3.6" height="6" fill="#fff"/></svg>
      mob: +44 7700 900 482
    </li>
    <li>
      <svg viewBox="0 0 12 12" aria-hidden="true"><circle cx="6" cy="6" r="6" fill="var(--accent)"/><rect x="2.8" y="4" width="6.4" height="4.2" fill="#fff"/></svg>
      colin@harbourlightceramics.example
    </li>
    <li>
      <svg viewBox="0 0 12 12" aria-hidden="true"><circle cx="6" cy="6" r="6" fill="var(--accent)"/><circle cx="6" cy="6" r="3.2" fill="none" stroke="#fff" stroke-width="1"/></svg>
      www.harbourlightceramics.example
    </li>
  </ul>
</section>

<section class="card card--back" aria-label="Business card back">
  <div class="back-identity">
    <p class="company-name">Harbourlight ceramics Ltd</p>
    <p class="back-identity__web">www.harbourlightceramics.example</p>
  </div>
</section>

</body>
</html>
```